Stationary & Business Card for a Rock climbing company based primarily in Joshua Tree NP
Use provided logo
Stationary & Business Card for a Rock climbing company based primarily in Joshua Tree NP - Outdoors
Creative Brief
Simple
Garrick Fenn
Director
27615 Marrow Lane Victorville, CA 92307
garrickfenn@mailbrook.com
www.ridgepathoutfitters.com

```html
<!DOCTYPE html>
<html lang="en">
<head>
<meta charset="utf-8">
<title>Ridgepath Outfitters – Business Card</title>
<link href="https://fonts.googleapis.com/css2?family=Open+Sans:wght@400;600;700&display=swap" rel="stylesheet">
<style>
  :root {
    --bg: #9c9c9c;
    --paper: #ffffff;
    --umber: #3e2f2a;
    --orange: #f0922a;
    --ink: #3a3a3a;
    --muted: #6b6b6b;
    --web: #e9e2dc;
  }
  * { box-sizing: border-box; margin: 0; padding: 0; }
  html, body { width: 1200px; height: 895px; overflow: hidden; }
  body {
    background: var(--bg);
    font-family: "Open Sans", Arial, sans-serif;
    display: flex;
    align-items: center;
    justify-content: center;
    gap: 40px;
  }
  .card {
    width: 540px;
    height: 309px;
    position: relative;
    overflow: hidden;
    box-shadow: 0 6px 18px rgba(0,0,0,.25);
  }

  /* Front */
  .card-front { background: var(--paper); }
  .band {
    position: absolute; left: 0; right: 0; height: 22px;
    background: var(--umber);
  }
  .band-top { top: 0; border-bottom: 3px solid var(--orange); }
  .band-bottom { bottom: 0; border-top: 3px solid var(--orange); }
  .brand {
    position: absolute; left: 34px; top: 64px; width: 190px;
    display: flex; flex-direction: column; align-items: center; gap: 14px;
  }
  .brand-mark {
    width: 104px; height: 104px; border-radius: 50%;
    background: var(--orange);
  }
  .brand-name {
    color: var(--umber); font-weight: 700; font-size: 19px;
    letter-spacing: 1.5px; text-transform: uppercase; text-align: center;
    line-height: 1.25;
  }
  .divider {
    position: absolute; left: 246px; top: 76px; width: 1px; height: 160px;
    background: #bdbdbd;
  }
  .contact { position: absolute; left: 262px; top: 74px; color: var(--ink); }
  .contact-name { font-size: 15px; font-weight: 600; }
  .contact-role { font-size: 11px; color: var(--muted); margin-bottom: 12px; }
  .contact-list { list-style: none; font-size: 10.5px; line-height: 1.35; }
  .contact-list li { display: flex; align-items: flex-start; gap: 7px; margin-bottom: 3px; }
  .contact-list svg { width: 12px; height: 12px; flex: none; margin-top: 1px; fill: var(--ink); }

  /* Back */
  .card-back { background: var(--umber); }
  .back-mark {
    position: absolute; left: 82px; top: 30px;
    width: 220px; height: 220px; border-radius: 50%;
    background: var(--orange);
  }
  .back-web {
    position: absolute; right: 30px; bottom: 22px;
    color: var(--web); font-size: 10.5px; letter-spacing: 1.2px;
  }
</style>
</head>
<body>

<section class="card card-front">
  <div class="band band-top"></div>

  <div class="brand">
    <div class="brand-mark"></div>
    <div class="brand-name">Ridgepath<br>Outfitters</div>
  </div>

  <div class="divider"></div>

  <div class="contact">
    <p class="contact-name">Garrick Fenn</p>
    <p class="contact-role">Director</p>
    <ul class="contact-list">
      <li>
        <svg viewBox="0 0 12 12"><path d="M6 0a4 4 0 0 0-4 4c0 3 4 8 4 8s4-5 4-8a4 4 0 0 0-4-4zm0 5.6A1.6 1.6 0 1 1 6 2.4a1.6 1.6 0 0 1 0 3.2z"/></svg>
        <span>27615 Marrow Lane<br>Victorville, CA 92307</span>
      </li>
      <li>
        <svg viewBox="0 0 12 12"><path d="M2.5 0.5l2 2.5-1 1.3a7 7 0 0 0 4.2 4.2l1.3-1 2.5 2-1.2 1.8C5 11 1 7 0.7 1.7z"/></svg>
        <span>(760) 415 2280</span>
      </li>
      <li>
        <svg viewBox="0 0 12 12"><path d="M2.5 0.5l2 2.5-1 1.3a7 7 0 0 0 4.2 4.2l1.3-1 2.5 2-1.2 1.8C5 11 1 7 0.7 1.7z"/></svg>
        <span>(760) 415 2291</span>
      </li>
      <li>
        <svg viewBox="0 0 12 12"><path d="M6 1C3 1 1 2.8 1 5c0 1.2.6 2.2 1.6 3L2 11l3-1.9c.3.1.7.1 1 .1 3 0 5-1.8 5-4.1S9 1 6 1z"/></svg>
        <span>gafenn</span>
      </li>
      <li>
        <svg viewBox="0 0 12 12"><path d="M0 2h12v8H0zm1 1v.4l5 3.3 5-3.3V3zm0 1.6V9h10V4.6L6 7.9z"/></svg>
        <span>garrickfenn@mailbrook.com</span>
      </li>
      <li>
        <svg viewBox="0 0 12 12"><path d="M6 0a6 6 0 1 0 0 12A6 6 0 0 0 6 0zm0 1.2c.7.8 1.2 2 1.4 3.4H4.6C4.8 3.2 5.3 2 6 1.2zM1.3 6.6h2.2c.1 1.3.4 2.5.9 3.5a4.8 4.8 0 0 1-3.1-3.5zm0-1.2a4.8 4.8 0 0 1 3.1-3.5c-.5 1-.8 2.2-.9 3.5zm4.7 5.4c-.7-.8-1.2-2-1.4-3.4h2.8c-.2 1.4-.7 2.6-1.4 3.4zm1.6-.7c.5-1 .8-2.2.9-3.5h2.2a4.8 4.8 0 0 1-3.1 3.5zm.9-4.7c-.1-1.3-.4-2.5-.9-3.5a4.8 4.8 0 0 1 3.1 3.5z"/></svg>
        <span>www.ridgepathoutfitters.com</span>
      </li>
    </ul>
  </div>

  <div class="band band-bottom"></div>
</section>

<section class="card card-back">
  <div class="back-mark" role="img" aria-label="Large orange circle brand emblem"></div>
  <p class="back-web">www.ridgepathoutfitters.com</p>
</section>

</body>
</html>
```